One Page / Executive Summary for Silverpine Executive Search

We would need an executive summary for our firm Silverpine Executive Search - like a small one pager which we can via PDF to our clients.
It should include like the file 23030 all Infos - Only Track Record needs to be complemented
But it should be designed much nicer than it is now - also open for new design situations but it should fit our website concept www.silverpinexs.io
It should also include a graph of the recruiting process - maybe draw a new one.?
We would need a very elegant, modern, slim design, it should look very female - it should not have a green color block on the top but be more sleek bright and with our bird
Target Market(s)
CEO, HR executives
Industry/Entity Type
HR Consultantcy
Other font styles liked:
- Calibri, cost or robotic condensed
Requirements
Must have
- sleek slim modern elegant design, ideally a white side with a frame or with our bird
Nice to have
- project progress on our website, female modern, elegant design, not too overloaded, possibility to complement our text
Should not have
- no petrol color block as on our website or as in our proposal, prefer a white background with our photo as a log,

```html
<!DOCTYPE html>
<html lang="en">
<head>
<meta charset="utf-8">
<title>Silverpine Executive Search – One Pager</title>
<link rel="stylesheet" href="https://fonts.googleapis.com/css2?family=Roboto+Condensed:wght@400;700&display=swap">
<style>
  :root{
    --canvas:#ecebe8;
    --paper:#ffffff;
    --sky:#c6e4f2;
    --teal:#1e6678;
    --teal-dark:#15505f;
    --navy:#1d4f6e;
    --coral:#ef4b3c;
    --ink:#24343c;
    --cyan:#17b4d4;
    --ph-teal:#12b2a8;
    --ph-orange:#f6b73c;
    --ph-pink:#ec4d84;
    --ph-purple:#c86ad0;
    --ph-green:#a6d653;
    --body:"Roboto Condensed", Arial, sans-serif;
  }
  *{box-sizing:border-box;margin:0;padding:0}
  html,body{width:1200px;height:750px;overflow:hidden;background:var(--canvas)}
  body{font-family:var(--body);color:var(--ink);font-weight:400}
  .page{position:absolute;left:338px;top:0;width:524px;height:750px;background:var(--paper);overflow:hidden;
        box-shadow:0 0 18px rgba(0,0,0,.12)}
  .abs{position:absolute}

  .tagline{left:291px;top:47px;width:233px;height:18px;background:var(--sky);color:var(--navy);
           font-size:7px;line-height:18px;padding-left:5px}
  .brand{left:150px;top:74px;width:310px;text-align:center;font-family:var(--body);font-weight:400;
         font-size:30px;line-height:34px;letter-spacing:0;color:var(--navy)}
  .values{left:190px;top:112px;width:230px;display:flex;justify-content:space-between;
          font-size:12px;color:var(--navy)}

  .tab-services{left:19px;top:143px;width:81px;height:18px;background:var(--coral);color:#fff;
                font-size:13px;font-weight:700;text-align:center;line-height:18px;border-radius:2px 2px 0 0}
  .panel-left{left:11px;top:161px;width:238px;height:275px;background:var(--sky)}
  .panel-right{left:273px;top:162px;width:220px;height:522px;background:var(--sky)}

  .label{background:var(--teal);color:#fff;font-size:11.5px;line-height:17px;padding-left:22px}
  .label::after{content:"";position:absolute;left:0;bottom:-5px;border-top:5px solid var(--teal-dark);border-left:6px solid transparent}
  .lbl-what{left:8px;top:174px;width:90px}
  .lbl-why{left:4px;top:279px;width:92px}
  .lbl-lead1{left:261px;top:174px;width:121px;padding-left:14px}
  .lbl-lead2{left:261px;top:263px;width:121px;padding-left:14px}
  .lbl-md{left:259px;top:364px;width:74px;line-height:14px;padding:3px 0 3px 5px}

  p,li{font-size:8px;line-height:10px;font-weight:400}
  .intro{left:30px;top:200px;width:210px}
  .industries{left:32px;top:228px;width:210px;display:grid;grid-template-columns:1fr 1fr;gap:0 4px}
  ul{list-style:none}
  li{position:relative;padding-left:8px}
  li::before{content:"•";position:absolute;left:0}
  .why{left:28px;top:302px;width:212px}
  .why li{font-size:7.3px;line-height:9.2px;text-align:justify}
  .lead-text{left:284px;top:198px;width:202px;text-align:justify;line-height:10.2px}
  .sectors{left:290px;top:286px;width:150px}
  .sectors li{line-height:10.5px}

  .process-bg{left:0;top:436px;width:272px;height:262px;background:linear-gradient(#fff,#f6f1e4)}
  .lbl-process{left:76px;top:443px;width:101px;height:23px;background:var(--teal);color:#fff;
               font-size:11.5px;line-height:23px;text-align:center}
  .chart{left:0;top:466px}
  .chart text{font-family:var(--body);fill:#fff;font-size:6px;font-weight:700}
  .chart .dark{fill:#5a4a12}

  .footer-red{left:0;top:684px;width:290px;height:14px;background:var(--coral);color:#fff;font-size:8px;
              line-height:14px;padding-left:14px}
  .footer-red b{margin-right:3px}
  .footer-red span{margin:0 3px}
  .footer-teal{left:0;top:698px;width:290px;height:52px;background:var(--teal)}
  .contacts{left:22px;top:710px;display:flex;gap:14px;color:#fff;font-size:8px;align-items:center}
  .contacts svg{vertical-align:-2px;margin-right:3px}

  .portrait{left:271px;top:333px;width:253px;height:417px;
            background:linear-gradient(180deg,rgba(198,228,242,0) 0%,#8a9aa2 30%,#1b1b1f 55%,#0c0c0f 100%)}
  .name{background:var(--coral);color:#fff;font-size:8px;line-height:13px;padding-left:4px}
  .name-a{left:421px;top:668px;width:103px}
  .name-b{left:341px;top:688px;width:183px}
</style>
</head>
<body>
<main class="page">
  <div class="abs tagline">So, they don't wear ties in the boardrooms anymore. We never did…</div>
  <div class="abs brand">Silverpine</div>
  <div class="abs values"><span>Honest</span><span>Personal</span><span>Pragmatic</span><span>Diverse</span></div>

  <div class="abs panel-left"></div>
  <div class="abs panel-right"></div>
  <div class="abs tab-services">Services</div>

  <div class="abs label lbl-what">What we do:</div>
  <p class="abs intro">While we consider ourselves a boutique Executive Search Firm our span across Europe and covers multiple industries:</p>
  <ul class="abs industries">
    <li>General Healthcare</li><li>Education</li>
    <li>Hospitals &amp; Medical Practices</li><li>Venture Capital</li>
    <li>Medical Technology</li><li>Private Equity</li>
    <li>Medical Association</li><li>Consumer</li>
  </ul>

  <div class="abs label lbl-why">Why us?</div>
  <ul class="abs why">
    <li>Longstanding experience with a passion for placing C-Level Executives</li>
    <li>We work with you personally and act as an ambassador for our clients in the market</li>
    <li>Engaging in at eye-level discussion beyond just placement and HR topics</li>
    <li>Structured, lean and, most importantly, transparent digital processes, with the opportunity of 24/7 self-update on search status in our online tool</li>
    <li>Creative search approaches and comprehensive candidate evaluation</li>
    <li>Through referencing of candidates as part of the process; psychometrics on demand</li>
  </ul>

  <div class="abs label lbl-lead1">Leadership Advisory</div>
  <p class="abs lead-text">Our Leadership advisory services are for Management Teams as well as HR-Professionals and candidates. They are designed to help you, and your organization, to build strong and effective leadership skills and teams that can drive growth, innovation, and success.</p>
  <div class="abs label lbl-lead2">Leadership Advisory</div>
  <ul class="abs sectors">
    <li>Healthcare</li><li>Private Capital</li><li>Consumer</li><li>Education &amp; Administration</li>
  </ul>

  <div class="abs process-bg"></div>
  <div class="abs lbl-process">Recruiting Process</div>
  <svg class="abs chart" width="262" height="210" viewBox="0 0 262 210" role="img" aria-label="Recruiting process in three phases">
    <rect x="2" y="0" width="92" height="21" fill="var(--cyan)"/>
    <rect x="96" y="0" width="99" height="21" fill="var(--cyan)"/>
    <rect x="197" y="0" width="63" height="21" fill="var(--cyan)"/>
    <text x="48" y="8" text-anchor="middle">Phase 1</text>
    <text x="48" y="16" text-anchor="middle">Research- LONGLIST</text>
    <text x="145" y="8" text-anchor="middle">Phase 2</text>
    <text x="145" y="16" text-anchor="middle">Fokus &amp; Interviews - SHORTLIST</text>
    <text x="228" y="9" text-anchor="middle">Phase 3</text>
    <text x="228" y="17" text-anchor="middle">Abschluss</text>

    <rect x="93" y="154" width="167" height="52" fill="var(--ph-green)"/>
    <rect x="197" y="21" width="63" height="140" fill="var(--ph-green)"/>
    <rect x="2" y="21" width="92" height="132" fill="var(--ph-orange)"/>
    <polygon points="4,21 44,21 44,72 79,72 79,111 4,111" fill="var(--ph-teal)"/>
    <rect x="96" y="21" width="98" height="133" fill="var(--ph-purple)"/>
    <polygon points="96,21 143,21 143,74 179,74 179,111 96,111" fill="var(--ph-pink)"/>
    <rect x="96" y="111" width="98" height="43" fill="var(--ph-pink)" opacity=".85"/>

    <text x="14" y="31">Kickoff</text>
    <line x1="22" y1="34" x2="22" y2="60" stroke="#fff" stroke-width=".6"/>
    <text x="6" y="84">Abstimmung Profil,</text>
    <text x="6" y="92">Positionsbeschreibung und</text>
    <text x="6" y="100">Zielfirmenliste.</text>
    <text x="60" y="34" class="dark">Research</text>
    <polyline points="70,37 70,44 84,44 84,126 80,126" fill="none" stroke="#5a4a12" stroke-width=".6"/>
    <text x="90" y="122" text-anchor="end" class="dark">Aktiver und passive</text>
    <text x="90" y="130" text-anchor="end" class="dark">Research, Ansprache pot.</text>
    <text x="90" y="138" text-anchor="end" class="dark">Kandidat·innen</text>

    <text x="100" y="32">Interviews</text>
    <line x1="108" y1="35" x2="108" y2="62" stroke="#fff" stroke-width=".6"/>
    <text x="100" y="84">Presentation der</text>
    <text x="100" y="92">priorisierten</text>
    <text x="100" y="100">Profile, Klienteninterviews</text>
    <text x="152" y="34">Referenzen</text>
    <polyline points="164,37 164,44 186,44 186,136 182,136" fill="none" stroke="#fff" stroke-width=".6"/>
    <text x="102" y="125">Ggf. Assessments, Einholen</text>
    <text x="102" y="133">von Referenzen</text>

    <text x="200" y="34" class="dark">Kandidatenauswahl</text>
    <polyline points="228,40 228,188 220,188" fill="none" stroke="#5a4a12" stroke-width=".6"/>
    <text x="215" y="183" text-anchor="end" class="dark">Vertragsverhandlung und</text>
    <text x="215" y="191" text-anchor="end" class="dark">Onboarding, Feedback- Gespräch</text>
  </svg>

  <div class="abs footer-red"><b>Locations:</b> Hamburg<span>▸</span>Wien<span>▸</span>München<span>▸</span>Düsseldorf</div>
  <div class="abs footer-teal"></div>
  <div class="abs contacts">
    <span><svg width="8" height="8" viewBox="0 0 10 10"><path d="M2 0.5 L4 2.8 L3 4 Q4.5 6 6 7 L7.2 6 L9.5 8 L8 9.6 Q3 9 0.4 2 Z" fill="#fff"/></svg>040 5521 9034</span>
    <span><svg width="9" height="7" viewBox="0 0 10 8"><rect x=".5" y=".5" width="9" height="7" fill="none" stroke="#fff"/><polyline points=".5,.5 5,4.5 9.5,.5" fill="none" stroke="#fff"/></svg>office@silverpinexs.io</span>
    <span><svg width="8" height="8" viewBox="0 0 10 10"><circle cx="5" cy="5" r="4.4" fill="none" stroke="#fff"/><ellipse cx="5" cy="5" rx="2" ry="4.4" fill="none" stroke="#fff"/><line x1=".6" y1="5" x2="9.4" y2="5" stroke="#fff"/></svg>www.silverpinexs.io</span>
  </div>

  <div class="abs portrait" role="img" aria-label="Photo of the two managing directors standing side by side in black tops"></div>
  <div class="abs label lbl-md">Managing<br>Directors</div>
  <div class="abs name name-a">Dr. Clara Westhoff-Brenner</div>
  <div class="abs name name-b">Marie Lindqvist</div>
</main>
</body>
</html>
```